Newsletter Landing Page Design

It's a landing page for a newsletter. Add the form on the landing page.

The landing page aims to drive conversions by encouraging visitors to sign up for the Betting Newsletter. It should convey the value proposition clearly and effectively to attract sports enthusiasts and avid bettors. The design should create a sense of trust, showcase the benefits of subscribing, and guide visitors towards the sign-up process with a user-friendly and visually appealing layout.

Key Elements and Considerations:
The landing page should feature a clean and modern design, utilizing minimalistic aesthetics and intuitive navigation to ensure a seamless user experience. The layout should prominently highlight the unique selling points of the Betting Newsletter, such as expert insights, valuable tips, exclusive promotions, and breaking news updates. Compelling imagery that resonates with the target audience should be incorporated to evoke excitement and credibility. The page should have a responsive design that adapts to different devices and screen sizes, making it accessible to users across platforms. Additionally, trust elements such as testimonials or affiliations with respected experts or organizations should be included to instill confidence. The sign-up process should be user-friendly, capturing essential information without overwhelming visitors. Privacy and data security should be emphasized, and analytics and tracking tools should be implemented for optimization purposes.

By incorporating these elements, the landing page will effectively communicate the value of the Betting Newsletter, provide a seamless user experience, and drive conversions by encouraging visitors to sign up.

Target Market(s)

People looking for Gambling information

Industry/Entity Type

Gambling

Number of Pages Required

1 page

Font styles to use
Sans Serif

Requirements
Must have
• Clean design, modern looking, not elementor looking
Nice to have
• Bold ideas, engaging, and features a human element

```html
<!DOCTYPE html>
<html lang="en">
<head>
<meta charset="utf-8">
<title>Betting Newsletter</title>
<link rel="stylesheet" href="https://fonts.googleapis.com/css2?family=Inter:wght@400;500;600;700;800&display=swap">
<style>
:root{
  --navy:#1c2233;
  --navy-deep:#141a28;
  --blue:#3b5fc0;
  --orange:#e7a046;
  --ink:#151821;
  --muted:#6b7080;
  --light:#f3f3f5;
  --white:#ffffff;
}
*{box-sizing:border-box;margin:0;padding:0}
html,body{width:1200px;height:2664px;overflow:hidden}
body{font-family:"Inter",sans-serif;color:var(--ink);background:var(--white);position:relative}
.abs{position:absolute;z-index:2}
.media{position:absolute;z-index:1}

/* hero */
.hero{position:absolute;left:0;top:0;width:1200px;height:560px;background:var(--navy)}
.brand-pill{left:140px;top:38px;width:140px;height:36px;border:2px solid rgba(255,255,255,.7);border-radius:18px}
.account{right:130px;top:44px;display:flex;align-items:center;gap:10px;color:#fff;font-size:13px;font-weight:500}
.account span.dot{width:22px;height:22px;border-radius:50%;background:#fff}
.hero h1{left:140px;top:116px;color:#fff;font-size:46px;line-height:1.15;font-weight:800}
.hero .lead{left:140px;top:240px;width:340px;color:#c9cdd8;font-size:13px;line-height:1.45}
.hero .lead b{color:var(--orange);font-weight:600;text-decoration:underline}
.field{height:42px;border-radius:21px;background:#fff;padding:0 18px;display:flex;align-items:center;font-size:12px;color:#9aa0ad}
.hero .f1{left:140px;top:306px;width:245px}
.hero .f2{left:140px;top:366px;width:245px}
.btn{display:flex;align-items:center;justify-content:center;height:42px;border-radius:21px;background:var(--orange);color:#fff;font-size:13px;font-weight:600}
.hero .btn{left:140px;top:424px;width:122px}
.hero-media{left:590px;top:40px;width:530px;height:480px;border-radius:50%/46%;background:radial-gradient(circle at 50% 60%,#3f6bd1 0,#2b4a9a 45%,#26314d 75%,transparent 76%)}

/* stats */
.stat{top:640px;width:200px}
.stat .num{font-size:82px;font-weight:700;color:var(--blue);line-height:1}
.stat .num sup{font-size:26px;font-weight:500;vertical-align:top;position:relative;top:30px;margin-left:4px}
.stat p{margin-top:14px;font-size:11px;line-height:1.4;color:var(--muted);width:160px}

/* expert tips */
.experts{position:absolute;left:0;top:835px;width:1200px;height:465px;background:var(--light)}
.experts h2{left:95px;top:110px;font-size:33px;font-weight:800;white-space:nowrap}
.experts .intro{left:95px;top:168px;width:420px;font-size:12px;line-height:1.5;color:var(--muted)}
.steps{left:95px;top:222px;list-style:none}
.steps li{display:flex;align-items:center;gap:12px;font-size:12px;color:var(--muted);height:34px}
.steps li i{width:20px;height:20px;border-radius:50%;background:var(--blue);color:#fff;font-style:normal;font-size:10px;font-weight:600;display:flex;align-items:center;justify-content:center}
.experts .field{left:95px;top:358px;width:290px;box-shadow:0 2px 8px rgba(0,0,0,.06)}
.experts .btn{left:345px;top:358px;width:120px;z-index:3}
.expert-media{left:660px;top:-55px;width:440px;height:520px;background:linear-gradient(180deg,#e9e3da 0,#c9d3e6 60%,#b7c4dc 100%);border-radius:220px 220px 0 0}

/* valuable tips */
.tips-title{left:140px;top:1440px;font-size:36px;font-weight:800;line-height:1.15}
.col{top:1435px;width:205px}
.col h3{font-size:16px;font-weight:700;line-height:1.3}
.col p{margin-top:10px;font-size:11px;line-height:1.55;color:var(--muted)}

/* promo band */
.band{position:absolute;left:0;top:1690px;width:1200px;height:430px;background:linear-gradient(90deg,var(--navy-deep) 0,#242b3c 55%,#1b2130 100%)}
.band h2{left:255px;top:90px;width:430px;color:#4f7de0;font-size:40px;font-weight:700;line-height:1.15}
.band p{left:255px;top:200px;width:430px;color:#b9bfcc;font-size:12px;line-height:1.6}
.band .btn{left:255px;top:300px;width:110px}
.phone-media{left:772px;top:1652px;width:190px;height:468px;border-radius:24px;background:linear-gradient(160deg,#3a5fb6 0,#1f2c4f 55%,#d9b79c 56%,#c9a589 100%)}

/* news */
.news-title{left:0;top:2190px;width:1200px;text-align:center;font-size:36px;font-weight:800}
.card{top:2285px;width:205px}
.card .thumb{width:205px;height:168px;border-radius:6px}
.card h4{margin-top:16px;font-size:16px;font-weight:700}
.card p{margin-top:8px;font-size:11px;line-height:1.5;color:var(--muted)}
</style>
</head>
<body>

<section class="hero">
  <div class="abs brand-pill"></div>
  <div class="abs account"><span class="dot"></span>Sign In Here</div>
  <h1 class="abs">Subscribe Now<br>to Our Newsletter</h1>
  <p class="abs lead">Get picks from 100,000+ bettors and weekly odds straight to your inbox, just <b>10 minutes reports</b></p>
  <div class="abs field f1">Enter Email Address</div>
  <div class="abs field f2">Full Name</div>
  <div class="abs btn">Subscribe</div>
  <div class="media hero-media" role="img" aria-label="Football players in action jumping for the ball in a stadium"></div>
</section>

<div class="abs stat" style="left:262px"><div class="num">99<sup>K</sup></div><p>Subscribers receive our weekly betting insight reports</p></div>
<div class="abs stat" style="left:520px"><div class="num">80<sup>%</sup></div><p>Win rate on expert picks across the last season games</p></div>
<div class="abs stat" style="left:770px"><div class="num">50.7</div><p>Average odds value shared with readers every month</p></div>

<section class="experts">
  <h2 class="abs">Get Exclusive Tips from Experts</h2>
  <p class="abs intro">Our analysts study every match, line and trend so you can place smarter bets with clear, simple advice each week.</p>
  <ul class="abs steps">
    <li><i>1</i>Daily match previews with key stats and form</li>
    <li><i>2</i>Expert value picks with odds and stake guide</li>
    <li><i>3</i>Early access to exclusive promotions and bonuses</li>
  </ul>
  <div class="abs field">Your Email Address</div>
  <div class="abs btn">Subscribe</div>
  <div class="media expert-media" role="img" aria-label="Excited man holding a football and a fan of banknotes"></div>
</section>

<h2 class="abs tips-title">Valuable<br>Tips</h2>
<div class="abs col" style="left:368px"><h3>Quis autem vel eum iure reprehenderit</h3><p>Nemo enim ipsam voluptatem quia voluptas sit aspernatur aut odit aut fugit, sed quia consequuntur magni dolores eos qui ratione voluptatem sequi nesciunt.</p></div>
<div class="abs col" style="left:596px"><h3>Quis autem vel eum iure reprehenderit</h3><p>Nemo enim ipsam voluptatem quia voluptas sit aspernatur aut odit aut fugit, sed quia consequuntur magni dolores eos qui ratione voluptatem sequi nesciunt.</p></div>
<div class="abs col" style="left:824px"><h3>Quis autem vel eum iure reprehenderit</h3><p>Nemo enim ipsam voluptatem quia voluptas sit aspernatur aut odit aut fugit, sed quia consequuntur magni dolores eos qui ratione voluptatem sequi nesciunt.</p></div>

<section class="band">
  <h2 class="abs">Quis autem vel eum iure reprehenderit</h2>
  <p class="abs">Nemo enim ipsam voluptatem quia voluptas sit aspernatur aut odit aut fugit, sed quia consequuntur magni dolores eos qui ratione voluptatem sequi nesciunt. Neque porro quisquam est, qui dolorem ipsum quia dolor sit amet.</p>
  <div class="abs btn">Presents</div>
</section>
<div class="media phone-media" role="img" aria-label="Hand holding a phone showing a football match"></div>

<h2 class="abs news-title">Breaking News Update</h2>
<div class="abs card" style="left:140px"><div class="thumb" role="img" aria-label="Football on a pitch near the goal" style="background:linear-gradient(160deg,#cfd6de,#6b8a4e)"></div><h4>Ratione Voluptatem</h4><p>Perspiciatis unde omnis iste natus error sit voluptatem accusantium.</p></div>
<div class="abs card" style="left:368px"><div class="thumb" role="img" aria-label="Footballer striking the ball" style="background:linear-gradient(160deg,#4d7bd0,#2a3b63)"></div><h4>Ratione Voluptatem</h4><p>Perspiciatis unde omnis iste natus error sit voluptatem accusantium.</p></div>
<div class="abs card" style="left:596px"><div class="thumb" role="img" aria-label="Football in flames on dark ground" style="background:linear-gradient(160deg,#e08a3a,#4a2616)"></div><h4>Ratione Voluptatem</h4><p>Perspiciatis unde omnis iste natus error sit voluptatem accusantium.</p></div>
<div class="abs card" style="left:824px"><div class="thumb" role="img" aria-label="Group of cheering football fans" style="background:linear-gradient(160deg,#8fc1e8,#e0a24c)"></div><h4>Ratione Voluptatem</h4><p>Perspiciatis unde omnis iste natus error sit voluptatem accusantium.</p></div>

</body>
</html>
```